Looking for an Innovative Print Design (Service Directory)

We need a new design for our advertisement within a printed colour services directory.

We are a compensation law firm called Velbrook Compensation Lawyers. Feel free to take a browse of our website www.velbrooklegal.com.au to get an idea of what we do and the kind of firm we are.

We are in the process of redeveloping our website and as such, so please don't adhere to the design principles of the current site- impress us with your originality!

On top of any editable formats, your final submissions must include a .pdf copy.
The same design will need to be presented in two dimensions:

- 154mm x 118mm (B1/B2 Half Page);
- 175mm x 113mm (B4 Half Page).

[For more information refer to attached Pdf.]

We have attached for you a few examples of other firms' designs (Sample1,2,3). These are by no means good, or what we're after, it's just to provide you with an idea of what sort of advertisements go into the service directory.

Hi all,

We want to emphasise that a priority of the design is that it must look:
• Professional
• Sophisticated
Please do not hesitate to use completely different colour schemes to the ones that are on our website- as we have said, our website will change in the near future, so cohesion between the current project and the website is not necessary!

Thanks!

Thank you for your submissions so far. There are some great ideas hidden in there. 

An issue we are having is that most of you are conforming to the same understanding of what it should look like. Remember that there is NO NEED to be bound by the image of firm as is. That is, feel free to use a different colour logo.

For inspiration, we relate well to the design aesthetics of: http://www.tinfernstudio.co.uk/

Look forward to seeing your 'out of the box' submissions. 

Reason: We've received a large amount of fantastic designs. However, what we're really looking for is something original. Please feel free to think outside the box (the final design doesn't need to look like a print ad), and construct a design that is completely incongruous with our website! While we do appreciate a minimalistic design, we have yet to receive something that really grabs your attention with its visuals. We're not sure but this may or may not be achieved with a full colour design. Thanks for all your submissions- they all have some features that really click with us. We look forward to the next wave of submissions!

Target Market(s)

We have various target markets, including mainly families, elderly people, blue collar workers.

These are individuals who are looking for assistance. They feel helpless or wronged.

Keep in mind that the people accessing these are those who prefer going to a printed directory rather than using a google search.

Industry/Entity Type

Law Firm

Font styles to use
Serif
Sans Serif

Requirements
Must have
• - Our name 'Velbrook Compensation Lawyers'
- Our logo (attached as logo.eps, logo.png, and logo.tif)
- Must include phone number as 1300 XXX XXX (this must be prominent)
- Must include the following service areas in these words: Motor vehicle claims, medical claims, superannuation claims, Workplace claims, negligence claims
- Our email address: info@velbrooklegal.com.au
- Our website address: www.velbrooklegal.com.au
- The following catchphrases: '98% success rate', and 'No win no fee' in those words
- Our location '412 Carvel Lane, Smithville, SYDNEY'
- For sizing dimensions, we need one in 154mm x 118mm and also a design in 175mm x 113mm (B4 Half Page) [refer to pdf attached]
Nice to have
• - Text indicating free initial consulatation
- Professional colour scheme
- As our website will be changed, do not worry about making the advertisement cohesive with our website design
- We want the design to be modern, but still professional
- Clean typeface
- No gradient colour scheme
- When designing, if you are looking to place more text onto the advertisement, these may be some considerations (feel free to change the wording): Accredited specialists, home and hospital visits

```html
<!DOCTYPE html>
<html lang="en">
<head>
<meta charset="utf-8">
<title>Velbrook Compensation Lawyers – Directory Advertisement</title>
<link rel="stylesheet" href="https://fonts.googleapis.com/css2?family=Montserrat:wght@300;400;700&family=Arimo:wght@400;700&display=swap">
<style>
  :root {
    --ink: #000000;
    --paper: #ffffff;
    --accent: #e0652a;
    --stone: #8a8482;
    --text-dark: #1a1a1a;
  }
  html, body {
    margin: 0;
    padding: 0;
    overflow: hidden;
    background: var(--paper);
  }
  .advert {
    display: block;
    width: 1200px;
    height: 920px;
  }
  .panel-accent { fill: var(--accent); }
  .panel-dark { fill: var(--ink); }

  .badge-ring { fill: none; stroke: var(--paper); stroke-width: 1.6; }
  .badge-text { fill: var(--paper); font-family: "Arimo", sans-serif; font-size: 25px; text-anchor: middle; }
  .badge-rule { stroke: var(--paper); stroke-width: 2.5; }

  .firm-name { fill: var(--paper); font-family: "Montserrat", sans-serif; font-weight: 300; font-size: 82px; letter-spacing: 9px; text-anchor: end; }
  .firm-descriptor { fill: var(--paper); font-family: "Montserrat", sans-serif; font-weight: 700; font-size: 26px; letter-spacing: 5.2px; text-anchor: end; }
  .phone { fill: var(--stone); font-family: "Arimo", sans-serif; font-weight: 700; font-size: 100px; text-anchor: end; letter-spacing: -1px; }
  .contact { fill: var(--stone); font-family: "Arimo", sans-serif; font-size: 24px; text-anchor: end; }

  .service { fill: var(--text-dark); font-family: "Arimo", sans-serif; font-size: 34px; }
  .service-rule { stroke: var(--accent); stroke-width: 3; }

  .sign-mark { fill: var(--accent); }
  .sign-name { fill: var(--stone); font-family: "Montserrat", sans-serif; font-weight: 400; }
  .sign-name-main { font-size: 48px; letter-spacing: 5px; }
  .sign-name-sub { font-size: 14.5px; letter-spacing: 3px; }
  .address { fill: var(--stone); font-family: "Arimo", sans-serif; font-size: 26px; }
</style>
</head>
<body>
<svg class="advert" viewBox="0 0 1200 920" xmlns="http://www.w3.org/2000/svg">
  <rect width="1200" height="920" fill="var(--paper)"/>

  <!-- Background panels -->
  <polygon class="panel-accent" points="0,0 312,0 388,326 0,388"/>
  <polygon class="panel-dark" points="310,0 1200,0 1200,638 484,720"/>

  <!-- Promise badge -->
  <g class="badge" transform="rotate(-9 165 172)">
    <circle class="badge-ring" cx="165" cy="172" r="112"/>
    <circle class="badge-ring" cx="165" cy="172" r="106"/>
    <text class="badge-text" x="165" y="138">98%</text>
    <text class="badge-text" x="165" y="166">Success Rate</text>
    <line class="badge-rule" x1="125" y1="182" x2="205" y2="182"/>
    <text class="badge-text" x="165" y="222">No Win No Fee</text>
  </g>

  <!-- Firm heading and contact -->
  <text class="firm-name" x="1094" y="232">VELBROOK</text>
  <text class="firm-descriptor" x="1090" y="263">COMPENSATION LAWYERS</text>
  <text class="phone" x="1088" y="362">1300 482 917</text>
  <text class="contact" x="1088" y="432">info@velbrooklegal.com.au</text>
  <text class="contact" x="1088" y="460">www.velbrooklegal.com.au</text>

  <!-- Service list -->
  <g class="services">
    <text class="service" x="62" y="512" transform="rotate(-9 62 512)">Motor vehicle claims</text>
    <line class="service-rule" x1="108" y1="527" x2="300" y2="497"/>
    <text class="service" x="65" y="590" transform="rotate(-9 65 590)">Medical claims</text>
    <line class="service-rule" x1="108" y1="606" x2="300" y2="576"/>
    <text class="service" x="66" y="666" transform="rotate(-9 66 666)">Superannuation claims</text>
    <line class="service-rule" x1="108" y1="686" x2="300" y2="656"/>
    <text class="service" x="63" y="742" transform="rotate(-9 63 742)">Workplace claims</text>
    <line class="service-rule" x1="108" y1="764" x2="300" y2="734"/>
    <text class="service" x="63" y="818" transform="rotate(-9 63 818)">Negligence claims</text>
    <line class="service-rule" x1="108" y1="843" x2="300" y2="813"/>
  </g>

  <!-- Sign-off -->
  <g class="sign-off">
    <circle class="sign-mark" cx="697" cy="778" r="40"/>
    <text class="sign-name sign-name-main" x="756" y="787">VELBROOK</text>
    <text class="sign-name sign-name-sub" x="758" y="808">COMPENSATION LAWYERS</text>
    <text class="address" x="582" y="855">412 Carvel Lane, Smithville, SYDNEY</text>
  </g>
</svg>
</body>
</html>
```